Nine Rung Ledger Remedy Seminar

I would like a flyer to hand out to participants at the speeches that we give. We are a CPA firm that specializes in entrepreneurs and realtors. We would like a flyer that looks crisp and clean, that integrates our logo and our company colors (shades of blue & gold). We would like the wording to be as laid out in the attached documents, but design is up to you. We would like a picture to go along with each point and are open to ideas. The flyer should be one page, preferably just the front.

Colors
3176b5
fee18a

Requirements
Must have
• Our logo and the wording supplied.
• A picture to go along with each topic.
Nice to have
• Images that pop, clean look, professional.
Should not have
• Look messy.

```html
<!DOCTYPE html>
<html lang="en">
<head>
<meta charset="utf-8">
<title>Nine Rung Ledger Remedy Seminar</title>
<link href="https://fonts.googleapis.com/css2?family=Arimo:wght@400;700&family=Oswald:wght@600&family=Tinos:ital,wght@1,700&display=swap" rel="stylesheet">
<style>
  :root {
    --blue: #3176b5;
    --blue-deep: #2458a0;
    --navy: #1f4e92;
    --gold: #fee18a;
    --gold-mid: #e2b95a;
    --gold-dark: #b8862b;
    --ink: #1c1c1c;
    --paper: #ffffff;
    --backdrop: #ecebe8;
    --wall-light: #f2f2f1;
    --wall-mid: #d9dadc;
    --wall-shade: #a9adb4;
    --floor: #c3c5c9;
  }
  * { margin: 0; padding: 0; box-sizing: border-box; }
  html, body { width: 1020px; height: 1200px; overflow: hidden; }
  body { background: var(--backdrop); font-family: "Arimo", Arial, sans-serif; }

  .sheet {
    position: absolute; left: 100px; top: 20px;
    width: 595px; height: 840px;
    transform: scale(1.38); transform-origin: 0 0;
    background: var(--paper); overflow: hidden;
    box-shadow: 0 2px 6px rgba(0,0,0,.15);
  }
  .hero-photo {
    position: absolute; left: 0; top: 0; width: 595px; height: 400px;
    background:
      radial-gradient(ellipse 70px 140px at 140px 290px, rgba(90,98,112,.55) 0%, rgba(90,98,112,0) 100%),
      radial-gradient(ellipse 240px 150px at 360px 150px, rgba(150,155,165,.45) 0%, rgba(150,155,165,0) 100%),
      linear-gradient(180deg, var(--wall-light) 0%, var(--wall-mid) 62%, var(--wall-shade) 72%, var(--floor) 74%, var(--floor) 100%);
  }
  .backdrop-shapes { position: absolute; left: 0; top: 0; width: 595px; height: 840px; }

  .brand { position: absolute; left: 23px; top: 22px; }
  .brand-name {
    font-family: "Arimo", Arial, sans-serif; font-weight: 700;
    font-size: 27px; color: var(--blue-deep); letter-spacing: -0.5px; line-height: 1;
  }
  .brand-tag {
    margin-top: 8px; font-family: "Tinos", serif; font-style: italic; font-weight: 700;
    font-size: 8.5px; color: var(--ink);
  }

  .agenda-title {
    position: absolute; left: 0; top: 368px; width: 595px; text-align: center;
    font-family: "Oswald", sans-serif; font-weight: 600; font-size: 20px;
    color: #fff; letter-spacing: .3px;
  }
  .agenda-rule {
    position: absolute; left: 53px; top: 398px; width: 488px; height: 1px;
    background: rgba(255,255,255,.7);
  }
  .agenda-rule::after {
    content: ""; position: absolute; left: 148px; top: -1px; width: 192px; height: 3px;
    background: var(--gold-mid);
  }

  .step {
    position: absolute; width: 115px; height: 155px;
    border-radius: 10px;
    background: linear-gradient(135deg, var(--gold-dark) 0%, var(--gold-mid) 35%, var(--gold) 60%, var(--gold-mid) 100%);
    padding: 30px 8px 6px; text-align: center;
    font-size: 8.2px; line-height: 1.22; color: var(--ink);
  }
  .step-num {
    position: absolute; left: 50%; top: 6px; transform: translateX(-50%);
    width: 17px; height: 17px; border-radius: 50%;
    background: var(--blue-deep); border: 1.5px solid #fff;
    color: #fff; font-weight: 700; font-size: 9px; line-height: 14px; text-align: center;
  }

  .tagline {
    position: absolute; left: 23px; top: 784px; width: 220px;
    font-weight: 700; font-size: 12.5px; line-height: 1.25; color: var(--navy);
  }
  .divider { position: absolute; left: 256px; top: 765px; width: 1px; height: 67px; background: #555; }
  .contact { position: absolute; left: 273px; top: 765px; font-size: 8px; color: var(--ink); font-style: normal; }
  .contact-firm { font-weight: 700; font-size: 10.5px; color: var(--navy); margin-bottom: 3px; }
  .contact-line { display: flex; align-items: center; gap: 4px; height: 12px; }
  .contact-line + .contact-line { margin-top: 1px; }
  .contact-pair { display: flex; align-items: center; gap: 4px; margin-right: 10px; }
  .icon { width: 9px; height: 9px; flex: none; }
</style>
</head>
<body>
<main class="sheet">
  <div class="hero-photo" role="img" aria-label="Photo of a man with raised arms facing a concrete wall sketched with a falling tax chart, money bag, clock and business doodles"></div>

  <svg class="backdrop-shapes" viewBox="0 0 595 840" aria-hidden="true">
    <defs>
      <linearGradient id="blueFill" x1="0" y1="0" x2="1" y2="1">
        <stop offset="0" stop-color="var(--blue-deep)"/>
        <stop offset="1" stop-color="var(--blue)"/>
      </linearGradient>
    </defs>
    <polygon points="0,365 86,250 138,315 208,265 273,320 333,275 393,340 463,300 513,320 595,235 595,610 0,770" fill="url(#blueFill)"/>
    <polyline points="0,365 86,250 138,315 208,265 273,320 333,275 393,340 463,300 513,320 595,235" fill="none" stroke="var(--gold-mid)" stroke-width="3"/>
  </svg>

  <div class="brand">
    <div class="brand-name">Steadfast Figures</div>
    <div class="brand-tag">A Professional Accounting Corporation</div>
  </div>

  <h1 class="agenda-title">NINE RUNG LEDGER REMEDY SEMINAR AGENDA:</h1>
  <div class="agenda-rule"></div>

  <section class="steps">
    <div class="step" style="left:23px;top:412px"><span class="step-num">1</span>We will first show you how to eliminate much of your self-employment tax on your return by converting your business into an S Corporation.A business owner making over $120,000 per year can save about $12,000 per year by doing this.</div>
    <div class="step" style="left:168px;top:412px"><span class="step-num">2</span>We will show you how to get tax free income from your corporation by renting you home to the corporation for the board meetings.Many of our clients are getting up to $21,000 in tax free income which could put $8,400 cash into your pocket</div>
    <div class="step" style="left:313px;top:412px"><span class="step-num">3</span>We will show you the easiest way to track your expenses so that the only thing you will have to do to have rock solid books is to take a picture of the receipt and throw it away. It doesn't get any better than that.</div>
    <div class="step" style="left:458px;top:412px"><span class="step-num">4</span>Next, we show you the importance of tax planning and why it is critical to meet with your CPA before the end of the year and not just when you do your tax preparation.</div>
    <div class="step" style="left:95px;top:585px"><span class="step-num">5</span>We will show you how to hire your children and get $7,500 per child tax free. This will save you $3,000 per child in income tax reduction</div>
    <div class="step" style="left:240px;top:585px"><span class="step-num">6</span>We will discuss how to make your child's college education tax deductible. With college cost spiraling out of control this is a biggie. Most of our clients have a savings of about $12,000 per year of college.</div>
    <div class="step" style="left:385px;top:585px"><span class="step-num">7</span>Our grand finale is to show you how to use, not one, but two corporations to get a several hundred thousand dollar tax deferral, get an interest free loan from the government and use that money to grow your business and your wealth.</div>
  </section>

  <p class="tagline">If they drive by with a machine gun you don't have to stand up.</p>
  <div class="divider"></div>

  <address class="contact">
    <div class="contact-firm">Steadfast Figures, A Professional Accounting Corporation</div>
    <div class="contact-line">820 N. Elm Ave, Ste. B, Lodi Creek, CA 95000</div>
    <div class="contact-line">
      <span class="contact-pair">
        <svg class="icon" viewBox="0 0 10 10"><circle cx="5" cy="5" r="5" fill="var(--navy)"/><path d="M3.3 2.6l1 1-.5.6c.3.7.8 1.2 1.5 1.5l.6-.5 1 1-.6.9C4.6 7 3 5.4 2.6 3.6z" fill="#fff"/></svg>555-014-2201
      </span>
      <span class="contact-pair">
        <svg class="icon" viewBox="0 0 10 10"><circle cx="5" cy="5" r="5" fill="var(--navy)"/><rect x="2.5" y="3.5" width="5" height="3.4" fill="#fff"/><rect x="3.4" y="2.4" width="3.2" height="1.3" fill="#fff"/></svg>555-014-2202
      </span>
    </div>
    <div class="contact-line">
      <span class="contact-pair">
        <svg class="icon" viewBox="0 0 10 10"><circle cx="5" cy="5" r="5" fill="var(--navy)"/><rect x="2.4" y="3.2" width="5.2" height="3.6" fill="#fff"/><path d="M2.4 3.2L5 5.2l2.6-2" fill="none" stroke="var(--navy)" stroke-width=".6"/></svg>Dana@steadfastfigurescpas.com
      </span>
      <span class="contact-pair">
        <svg class="icon" viewBox="0 0 10 10"><circle cx="5" cy="5" r="5" fill="var(--navy)"/><rect x="2.4" y="3.2" width="5.2" height="3.6" fill="#fff"/><path d="M2.4 3.2L5 5.2l2.6-2" fill="none" stroke="var(--navy)" stroke-width=".6"/></svg>Reese@steadfastfigurescpas.com
      </span>
    </div>
    <div class="contact-line">
      <svg class="icon" viewBox="0 0 10 10"><circle cx="5" cy="5" r="5" fill="var(--navy)"/><circle cx="5" cy="5" r="2.8" fill="none" stroke="#fff" stroke-width=".7"/><path d="M2.2 5h5.6M5 2.2c-1.4 1.6-1.4 4 0 5.6M5 2.2c1.4 1.6 1.4 4 0 5.6" fill="none" stroke="#fff" stroke-width=".5"/></svg>www.steadfastfigurescpa.com
    </div>
  </address>
</main>
</body>
</html>
```